Timeline flyer

Hi, we are an agency, our business is to orienteates student to study abroad in Germany. For that, we enroll them in language schools in Germany and help them to find an accomodation.
Students are always lost we thinked about a timeline to help them figure out what they have to do once in Germany so they don't miss delays.
You can find in the attachement an example that i made in powerpoint but it's really basic and it's only for u so you can understant what the timeline should look like.
We need two time lines.
For the first one (file first timeline)
Title : Procédure pour intégrer le semestre d’hiver dans les universités Allemandes
The first paragraph (up on the left in my proposition) : L’étudiant devra pendant ces mois débuter ses cours d’allemand en Tunisie et les poursuivre en Allemagne après l’obtention du Visa d’étude. L’atteinte du niveau C1 est primordiale pour la bonne réussite du test Kel ou le PLQ.
The second paragraph (below on the left in my proposition) : L’étudiant devra à cette date avoir déjà passer le test KEL ou le PLQ pour pouvoir être à temps pour les inscriptions universitaires. Il faut compter 6 semaines pour le test Kel et 2 à 3 semaines pour obtenir les résultats des tests.
The third one (up on the right in my proposition) : Le dernier délais d’inscription pour pouvoir intégrer une université Allemande pendant la rentrée hivernale (15 Octobre).
The last one (below on the right in my proposition) : Rentrée universitaire
For the second one (file second timeline) :
Title : Procédure pour intégrer le semestre d’été dans les universités Allemandes *
The third one (up on the right in my proposition) : Le dernier délais d’inscription pour pouvoir intégrer une université Allemande pendant la rentrée estivale (15 Avril).
There is also an additional sentence below in the right for this one : * Les spécialités assurées pendant les semestres d’été sont limitées.
You can also find in the attachement our flyers (so you can inspire youself with the color and the design), we want our student to recognize that the flyer is related to our agency so please try to use colors that are matched with the other flyer.
Also, you can find our Logo in the attachement.
Thank you :)
Waiting for your propositions ! :)

```html
<!DOCTYPE html>
<html lang="fr">
<head>
<meta charset="utf-8">
<title>Timeline flyers – Nordweg Centre</title>
<link href="https://fonts.googleapis.com/css2?family=Oswald:wght@500;700&family=Open+Sans:wght@400;600&display=swap" rel="stylesheet">
<style>
  :root{
    --olive:#8b8f2b;
    --olive-dark:#5f6318;
    --lime:#c9d41c;
    --lime-soft:#d9e05a;
    --gold:#c9ad34;
    --grey:#a9aaa6;
    --grey-light:#d3d4d0;
    --paper:#f4f4f2;
    --ink:#3a3b35;
    --stage:#e8e6e1;
  }
  *{box-sizing:border-box;margin:0;padding:0}
  html,body{width:1200px;height:675px;overflow:hidden;background:var(--stage)}
  .stage{position:relative;width:1200px;height:675px}
  .flyer{position:absolute;top:136px;width:570px;height:403px;background:var(--paper);overflow:hidden;box-shadow:0 2px 10px rgba(0,0,0,.12)}
  .flyer--winter{left:20px}
  .flyer--summer{left:610px}

  .title-band{position:absolute;left:0;top:18px;width:552px;height:30px;background:var(--olive);
    clip-path:polygon(0 0,100% 0,95% 100%,0 100%);
    font-family:'Oswald',sans-serif;font-weight:700;font-size:12.5px;color:#fff;text-transform:uppercase;
    letter-spacing:.2px;line-height:30px;padding-left:16px;padding-right:34px;white-space:nowrap}
  .edge-strip{position:absolute;right:0;top:4px;width:130px;height:11px;background:var(--grey);
    clip-path:polygon(10% 0,100% 0,100% 100%,0 100%)}
  .corner-strip{position:absolute;left:0;bottom:38px;width:90px;height:14px;background:var(--grey-light);
    clip-path:polygon(0 0,80% 0,100% 100%,0 100%)}
  .contact-band{position:absolute;left:110px;right:0;bottom:0;height:34px;background:var(--lime);
    clip-path:polygon(6% 0,100% 0,100% 100%,0 100%);
    font-family:'Open Sans',sans-serif;font-weight:600;font-size:9px;color:var(--ink);
    display:flex;align-items:center;justify-content:flex-end;padding-right:18px;gap:14px}
  .contact-rule{position:absolute;left:140px;right:0;bottom:34px;height:3px;background:var(--olive)}

  .brand{position:absolute;left:18px;top:196px;display:flex;align-items:center;gap:6px}
  .brand-dot{width:22px;height:22px;border-radius:50%;background:var(--lime)}
  .brand-name{font-family:'Oswald',sans-serif;font-weight:700;font-size:17px;line-height:1;color:var(--ink);width:86px}

  .timeline{position:absolute;left:0;top:0;width:570px;height:403px}
  .tl-label{font-family:'Oswald',sans-serif;font-weight:700;fill:var(--olive-dark);text-anchor:middle}
  .tl-year{font-size:8.5px}
  .tl-month{font-size:7.5px;font-weight:500}

  .note{position:absolute;border:1.5px solid var(--lime-soft);background:var(--paper);
    font-family:'Open Sans',sans-serif;font-size:7px;line-height:1.35;color:var(--ink);padding:6px 7px}
  .note--months{left:150px;top:62px;width:182px}
  .note--deadline{left:347px;top:62px;width:134px}
  .note--exam{left:296px;top:262px;width:168px}
  .note--start{left:478px;top:262px;width:80px;text-align:center;font-weight:600}
  .footnote{position:absolute;top:300px;left:150px;width:140px;font-family:'Open Sans',sans-serif;
    font-size:6.5px;line-height:1.3;color:var(--ink)}
</style>
</head>
<body>
<main class="stage">

  <section class="flyer flyer--winter">
    <div class="edge-strip"></div>
    <h1 class="title-band">Procédure pour intégrer le semestre d’hiver dans les universités allemandes</h1>
    <div class="corner-strip"></div>

    <div class="brand"><span class="brand-dot"></span><span class="brand-name">Nordweg Centre</span></div>

    <svg class="timeline" viewBox="0 0 570 403" aria-hidden="true">
      <defs>
        <linearGradient id="linkW" x1="0" y1="0" x2="0" y2="1">
          <stop offset="0" stop-color="#d6d64a"/><stop offset="1" stop-color="#c9ad34"/>
        </linearGradient>
      </defs>
      <path d="M241 140 V152 M187 152 H349 M187 152 V172 M349 152 V172" stroke="url(#linkW)" stroke-width="1.3" fill="none"/>
      <path d="M430 125 V215" stroke="url(#linkW)" stroke-width="1.3"/>
      <path d="M376 262 V250" stroke="url(#linkW)" stroke-width="1.3"/>
      <path d="M511 262 V222" stroke="url(#linkW)" stroke-width="1.3"/>
      <line x1="150" y1="215" x2="548" y2="215" stroke="#b9bab5" stroke-width="3"/>
      <polygon points="548,209 560,215 548,221" fill="#b9bab5"/>
      <g fill="#f4f4f2" stroke="#d2d65a" stroke-width="1.3">
        <circle cx="160" cy="215" r="3.2"/><circle cx="187" cy="215" r="3.2"/><circle cx="214" cy="215" r="3.2"/>
        <circle cx="241" cy="215" r="3.2"/><circle cx="268" cy="215" r="3.2"/><circle cx="295" cy="215" r="3.2"/>
        <circle cx="322" cy="215" r="3.2"/><circle cx="349" cy="215" r="3.2"/><circle cx="376" cy="215" r="3.2"/>
        <circle cx="403" cy="215" r="3.2"/><circle cx="430" cy="215" r="3.2"/><circle cx="457" cy="215" r="3.2"/>
        <circle cx="484" cy="215" r="3.2"/><circle cx="511" cy="215" r="3.2"/><circle cx="538" cy="215" r="3.2"/>
      </g>
      <g class="tl-label">
        <text x="187" y="190" class="tl-month">Oct</text><text x="187" y="201" class="tl-year">2016</text>
        <text x="241" y="190" class="tl-month">Déc</text><text x="241" y="201" class="tl-year">2016</text>
        <text x="295" y="190" class="tl-month">Fév</text><text x="295" y="201" class="tl-year">2017</text>
        <text x="349" y="190" class="tl-month">Avr</text><text x="349" y="201" class="tl-year">2017</text>
        <text x="403" y="190" class="tl-month">Jui</text><text x="403" y="201" class="tl-year">2017</text>
        <text x="457" y="190" class="tl-month">Août</text><text x="457" y="201" class="tl-year">2017</text>
        <text x="511" y="190" class="tl-month">18 Octobre</text><text x="511" y="201" class="tl-year">2017</text>
      </g>
      <g class="tl-label">
        <text x="160" y="235" class="tl-year">2016</text><text x="160" y="245" class="tl-month">Sep</text>
        <text x="214" y="235" class="tl-year">2016</text><text x="214" y="245" class="tl-month">Nov</text>
        <text x="268" y="235" class="tl-year">2017</text><text x="268" y="245" class="tl-month">Jan</text>
        <text x="322" y="235" class="tl-year">2017</text><text x="322" y="245" class="tl-month">Mars</text>
        <text x="376" y="235" class="tl-year">2017</text><text x="376" y="245" class="tl-month">Début Mai</text>
        <text x="430" y="235" class="tl-year">2017</text><text x="430" y="245" class="tl-month">15 Juillet</text>
        <text x="484" y="235" class="tl-year">2017</text><text x="484" y="245" class="tl-month">Sep</text>
        <text x="538" y="235" class="tl-year">2017</text><text x="538" y="245" class="tl-month">Nov</text>
      </g>
    </svg>

    <p class="note note--months">L’étudiant devra pendant ces mois débuter ses cours d’allemand en Tunisie et les poursuivre en Allemagne après l’obtention du Visa d’étude. L’atteinte du niveau C1 est primordiale pour la bonne réussite du test Kel ou le PLQ.</p>
    <p class="note note--deadline">Le dernier délais d’inscription pour pouvoir intégrer une université Allemande pendant la rentrée hivernale (15 Octobre).</p>
    <p class="note note--exam">L’étudiant devra à cette date avoir déjà passer le test KEL ou le PLQ pour pouvoir être à temps pour les inscriptions universitaires. Il faut compter 6 semaines pour le test Kel et 2 à 3 semaines pour obtenir les résultats des tests.</p>
    <p class="note note--start">Rentrée universitaire</p>

    <div class="contact-rule"></div>
    <footer class="contact-band"><span>Tél : 71 000 000</span><span>12 rue des Tilleuls, Tunis</span><span>contact@nordweg-centre.tn</span></footer>
  </section>

  <section class="flyer flyer--summer">
    <div class="edge-strip"></div>
    <h1 class="title-band">Procédure pour intégrer le semestre d’été dans les universités allemandes *</h1>
    <div class="corner-strip"></div>

    <div class="brand"><span class="brand-dot"></span><span class="brand-name">Nordweg Centre</span></div>

    <svg class="timeline" viewBox="0 0 570 403" aria-hidden="true">
      <defs>
        <linearGradient id="linkS" x1="0" y1="0" x2="0" y2="1">
          <stop offset="0" stop-color="#d6d64a"/><stop offset="1" stop-color="#c9ad34"/>
        </linearGradient>
      </defs>
      <path d="M241 140 V152 M187 152 H349 M187 152 V172 M349 152 V172" stroke="url(#linkS)" stroke-width="1.3" fill="none"/>
      <path d="M430 125 V215" stroke="url(#linkS)" stroke-width="1.3"/>
      <path d="M376 262 V250" stroke="url(#linkS)" stroke-width="1.3"/>
      <path d="M511 262 V222" stroke="url(#linkS)" stroke-width="1.3"/>
      <line x1="150" y1="215" x2="548" y2="215" stroke="#b9bab5" stroke-width="3"/>
      <polygon points="548,209 560,215 548,221" fill="#b9bab5"/>
      <g fill="#f4f4f2" stroke="#d2d65a" stroke-width="1.3">
        <circle cx="160" cy="215" r="3.2"/><circle cx="187" cy="215" r="3.2"/><circle cx="214" cy="215" r="3.2"/>
        <circle cx="241" cy="215" r="3.2"/><circle cx="268" cy="215" r="3.2"/><circle cx="295" cy="215" r="3.2"/>
        <circle cx="322" cy="215" r="3.2"/><circle cx="349" cy="215" r="3.2"/><circle cx="376" cy="215" r="3.2"/>
        <circle cx="403" cy="215" r="3.2"/><circle cx="430" cy="215" r="3.2"/><circle cx="457" cy="215" r="3.2"/>
        <circle cx="484" cy="215" r="3.2"/><circle cx="511" cy="215" r="3.2"/><circle cx="538" cy="215" r="3.2"/>
      </g>
      <g class="tl-label">
        <text x="187" y="190" class="tl-month">Avr</text><text x="187" y="201" class="tl-year">2017</text>
        <text x="241" y="190" class="tl-month">Juin</text><text x="241" y="201" class="tl-year">2017</text>
        <text x="295" y="190" class="tl-month">Août</text><text x="295" y="201" class="tl-year">2017</text>
        <text x="349" y="190" class="tl-month">Oct</text><text x="349" y="201" class="tl-year">2017</text>
        <text x="403" y="190" class="tl-month">Déc</text><text x="403" y="201" class="tl-year">2017</text>
        <text x="457" y="190" class="tl-month">Fév</text><text x="457" y="201" class="tl-year">2018</text>
        <text x="511" y="190" class="tl-month">15 Avril</text><text x="511" y="201" class="tl-year">2018</text>
      </g>
      <g class="tl-label">
        <text x="160" y="235" class="tl-year">2017</text><text x="160" y="245" class="tl-month">Mars</text>
        <text x="214" y="235" class="tl-year">2017</text><text x="214" y="245" class="tl-month">Mai</text>
        <text x="268" y="235" class="tl-year">2017</text><text x="268" y="245" class="tl-month">Juil</text>
        <text x="322" y="235" class="tl-year">2017</text><text x="322" y="245" class="tl-month">Sep</text>
        <text x="376" y="235" class="tl-year">2017</text><text x="376" y="245" class="tl-month">Début Nov</text>
        <text x="430" y="235" class="tl-year">2018</text><text x="430" y="245" class="tl-month">Jan</text>
        <text x="484" y="235" class="tl-year">2018</text><text x="484" y="245" class="tl-month">Mars</text>
        <text x="538" y="235" class="tl-year">2018</text><text x="538" y="245" class="tl-month">Mai</text>
      </g>
    </svg>

    <p class="note note--months">L’étudiant devra pendant ces mois débuter ses cours d’allemand en Tunisie et les poursuivre en Allemagne après l’obtention du Visa d’étude. L’atteinte du niveau C1 est primordiale pour la bonne réussite du test Kel ou le PLQ.</p>
    <p class="note note--deadline">Le dernier délais d’inscription pour pouvoir intégrer une université Allemande pendant la rentrée estivale (15 Avril).</p>
    <p class="note note--exam">L’étudiant devra à cette date avoir déjà passer le test KEL ou le PLQ pour pouvoir être à temps pour les inscriptions universitaires. Il faut compter 6 semaines pour le test Kel et 2 à 3 semaines pour obtenir les résultats des tests.</p>
    <p class="note note--start">Rentrée universitaire</p>
    <p class="footnote">* Les spécialités assurées pendant les semestres d’été sont limitées.</p>

    <div class="contact-rule"></div>
    <footer class="contact-band"><span>Tél : 71 000 000</span><span>12 rue des Tilleuls, Tunis</span><span>contact@nordweg-centre.tn</span></footer>
  </section>

</main>
</body>
</html>
```